VoxTend Needs a Business Card

We need a business card for Tomas Belcourt, Ph.D., CCC-SLP, who is affiliated with Harrowfield Crest University. He is an Associate Professor and Licensed Speech-Language Pathologist, Department of Communication Disorders, College of Health and Human Services.

He has a consulting business "VoxTend Consultant". The logo is attached. The consulting company color is Turquoise. HCU school color is orange.

The consulting business focus on: Consultation, Research & Professional Development. Our target market is individuals with annual family income of $100,000.00 or more for consultation and speech-language pathologists for professional development activities.

No harsh colors, subtle colors appreciated. Address, e-mail, telephone, and small scan logo for a link to our website. Creativity in design will be appreciated. Please add your comments, why you created this design?

Thanks and looking for submissions.

```html
<!DOCTYPE html>
<html lang="en">
<head>
<meta charset="utf-8">
<title>VoxTend Consultant — Business Card</title>
<link href="https://fonts.googleapis.com/css2?family=Open+Sans:wght@400;600;700&display=swap" rel="stylesheet">
<style>
  :root {
    --turquoise: #4cc5cc;
    --turquoise-deep: #3fb6be;
    --turquoise-light: #bfeaec;
    --grey-bg: #e6e6e6;
    --card-white: #fbfbfb;
    --ink: #3a3a3a;
    --ink-soft: #555;
    --green: #3db54a;
  }
  * { box-sizing: border-box; margin: 0; padding: 0; }
  html, body { width: 1200px; height: 1200px; overflow: hidden; }
  body {
    background: radial-gradient(circle at 40% 30%, #f4f4f4 0%, var(--grey-bg) 75%);
    font-family: "Open Sans", sans-serif;
    display: flex;
    flex-direction: column;
    align-items: center;
    justify-content: center;
    gap: 60px;
  }
  .card {
    width: 630px;
    height: 360px;
    position: relative;
    overflow: hidden;
    box-shadow: 0 6px 18px rgba(0,0,0,0.12);
  }

  /* Front */
  .card-front {
    background: var(--turquoise);
    display: flex;
    align-items: center;
    justify-content: center;
  }
  .front-brand {
    display: flex;
    align-items: center;
    gap: 18px;
  }
  .brand-square {
    width: 46px; height: 46px;
    background: #ffffff;
  }
  .front-brand .brand-name {
    font-size: 52px;
    font-weight: 400;
    color: #ffffff;
    letter-spacing: 0.5px;
  }

  /* Back */
  .card-back { background: var(--card-white); }
  .back-brand {
    position: absolute;
    top: 44px; right: 44px;
    display: flex;
    align-items: center;
    gap: 12px;
  }
  .back-brand .brand-square {
    width: 30px; height: 30px;
    background: var(--turquoise);
  }
  .back-brand .brand-name {
    font-size: 30px;
    font-weight: 400;
    color: var(--turquoise-deep);
  }
  .name-band {
    position: absolute;
    top: 138px; left: 0; right: 0;
    height: 46px;
    background: var(--turquoise);
    display: flex;
    align-items: center;
    padding-left: 40px;
    gap: 22px;
  }
  .holder-name {
    font-size: 19px;
    font-weight: 700;
    color: var(--turquoise-light);
  }
  .credentials {
    font-size: 13px;
    line-height: 1.25;
    color: var(--turquoise-light);
  }
  .address {
    position: absolute;
    top: 204px; left: 40px;
    font-size: 14px;
    line-height: 1.35;
    color: var(--ink-soft);
  }
  .contact-list {
    position: absolute;
    top: 200px; left: 250px;
    border-left: 1px solid #9a9a9a;
    padding-left: 12px;
    list-style: none;
    display: flex;
    flex-direction: column;
    gap: 6px;
  }
  .contact-list li {
    display: flex;
    align-items: center;
    gap: 9px;
    font-size: 17px;
    color: var(--ink);
  }
  .contact-icon { width: 16px; height: 16px; flex: none; }
  .bottom-band {
    position: absolute;
    left: 0; right: 0; bottom: 46px;
    height: 14px;
    background: var(--turquoise);
  }
</style>
</head>
<body>

  <section class="card card-front" aria-label="Card front">
    <div class="front-brand">
      <span class="brand-square"></span>
      <span class="brand-name">VoxTend</span>
    </div>
  </section>

  <section class="card card-back" aria-label="Card back">
    <div class="back-brand">
      <span class="brand-square"></span>
      <span class="brand-name">VoxTend</span>
    </div>

    <div class="name-band">
      <span class="holder-name">Tomas Belcourt</span>
      <span class="credentials">Ph.D. CCC-SLP<br>Speech-Language Pathologist</span>
    </div>

    <p class="address">318 W Larkspur Ave.,<br>Chicago IL 60614</p>

    <ul class="contact-list">
      <li>
        <svg class="contact-icon" viewBox="0 0 16 16" aria-hidden="true">
          <circle cx="8" cy="8" r="8" fill="var(--green)"/>
          <circle cx="8" cy="8" r="4.5" fill="none" stroke="#fff" stroke-width="1"/>
          <ellipse cx="8" cy="8" rx="2" ry="4.5" fill="none" stroke="#fff" stroke-width="1"/>
          <line x1="3.5" y1="8" x2="12.5" y2="8" stroke="#fff" stroke-width="1"/>
        </svg>
        www.voxtendconsult.com
      </li>
      <li>
        <svg class="contact-icon" viewBox="0 0 16 16" aria-hidden="true">
          <circle cx="8" cy="8" r="8" fill="var(--green)"/>
          <rect x="4" y="5" width="8" height="6" fill="none" stroke="#fff" stroke-width="1"/>
          <polyline points="4,5 8,8.5 12,5" fill="none" stroke="#fff" stroke-width="1"/>
        </svg>
        tomas@voxtendconsult.com
      </li>
      <li>
        <svg class="contact-icon" viewBox="0 0 16 16" aria-hidden="true">
          <circle cx="8" cy="8" r="8" fill="var(--green)"/>
          <path d="M5.5 4.5 L7 4.5 L7.6 6.6 L6.7 7.3 Q7.5 8.8 8.7 9.4 L9.4 8.5 L11.5 9.1 L11.5 10.6 Q8 11.5 5.5 7.5 Z" fill="#fff"/>
        </svg>
        1-888-555-0142
      </li>
    </ul>

    <div class="bottom-band"></div>
  </section>

</body>
</html>
```